Verdant QUICK Repairs Business card

Harbison Motors is looking for a business card design for our detailing wing "Verdant QUICK Repairs"
The services offered are vehicle paintless dent repairs, vehicle detailing, scratch and bumper repairs & paint and alloy wheel repairs.
Ideally the card design should be sharp, neat and professional. We are not looking for a card with pictures of cars.
Our corporate colours are blues (as in the logo supplied) which may look good with water droplets in high res and perhaps one or two images leaking off the card. Dark blacks with electric blues perhaps.
Images may be of a spray gun (we use Carrowmist), a rotary polisher (Trevalo Orbix) or similar objects used in the processes.

Industry/Entity Type

Paint

Contact Information for Business Card

Title: Verdant QUICK Repairs
Services: Bumper Repairs
Scratch/Paint Repairs
Paintless dent repairs
Alloy wheel repairs
Name: Martin K
Telephone: 0427195063
Email : martin@harbisonmotors.com.au

Font styles to use
Sans Serif
Other font styles liked:

Colors
0355a3
3277b5
0792cd
cfdfed

Requirements
Must have
• The title - "Verdant QUICK Repairs" should be a focus on either the from or back of the card
Should not have
• Photographs of cars

```html
<!DOCTYPE html>
<html lang="en">
<head>
<meta charset="utf-8">
<title>Verdant QUICK Repairs – Business Card</title>
<link rel="stylesheet" href="https://fonts.googleapis.com/css2?family=Roboto+Slab:wght@800;900&family=Archivo+Black&display=swap">
<style>
  :root {
    --page: #ffffff;
    --card-edge: #000000;
    --ink: #0a0a0a;
    --teal-top: #0a7dad;
    --navy-mid: #1f4f86;
    --plum-deep: #2b2250;
    --beam-top: #1d6db6;
    --beam-bottom: #29a9e1;
    --wave-light: #0a86b8;
    --wave-mid: #1b5f95;
    --tool-dark: #0b1220;
  }
  html, body {
    margin: 0;
    padding: 0;
    width: 1200px;
    height: 722px;
    overflow: hidden;
    background: var(--page);
  }
  .card-sheet { display: block; width: 1200px; height: 722px; }
  .title-text { font-family: "Roboto Slab", Georgia, serif; font-weight: 900; fill: var(--ink); }
  .services-text { font-family: "Roboto Slab", Georgia, serif; font-weight: 800; fill: var(--ink); }
  .contact-text { font-family: "Archivo Black", "Arial Black", sans-serif; fill: var(--ink); }
  .icon { fill: var(--ink); }
</style>
</head>
<body>
<svg class="card-sheet" viewBox="0 0 1200 722" xmlns="http://www.w3.org/2000/svg">
  <defs>
    <linearGradient id="front-bg" x1="0" y1="0" x2="0" y2="1">
      <stop offset="0" stop-color="var(--teal-top)"/>
      <stop offset="0.55" stop-color="var(--navy-mid)"/>
      <stop offset="1" stop-color="var(--plum-deep)"/>
    </linearGradient>
    <linearGradient id="beam" x1="0" y1="0" x2="0" y2="1">
      <stop offset="0" stop-color="var(--beam-top)"/>
      <stop offset="1" stop-color="var(--beam-bottom)"/>
    </linearGradient>
    <linearGradient id="back-bg" x1="0" y1="0" x2="1" y2="0">
      <stop offset="0" stop-color="var(--plum-deep)"/>
      <stop offset="0.5" stop-color="var(--wave-mid)"/>
      <stop offset="1" stop-color="var(--plum-deep)"/>
    </linearGradient>
    <linearGradient id="tool-fill" x1="0" y1="0" x2="1" y2="0">
      <stop offset="0" stop-color="var(--tool-dark)"/>
      <stop offset="1" stop-color="#16243a"/>
    </linearGradient>
    <clipPath id="back-clip"><rect x="454" y="343" width="635" height="334" rx="28"/></clipPath>
  </defs>

  <!-- Front card -->
  <g class="card-front">
    <rect x="30" y="22" width="363" height="668" rx="40" fill="var(--card-edge)"/>
    <rect x="46" y="38" width="331" height="636" rx="30" fill="url(#front-bg)"/>
    <polygon class="spray-beam" points="205,160 209,160 353,674 58,674" fill="url(#beam)"/>
    <rect class="tool-area" x="108" y="50" width="178" height="110" rx="14" fill="url(#tool-fill)" opacity="0.85"
          role="img" aria-label="Silhouette of a paint spray gun aiming downward"/>
    <text class="title-text" x="212" y="420" font-size="44" text-anchor="middle"
          textLength="310" lengthAdjust="spacingAndGlyphs">Verdant QUICK Repairs</text>
    <text class="services-text" x="211" y="471" font-size="15" text-anchor="middle"
          textLength="322" lengthAdjust="spacingAndGlyphs">Bumper Repairs Scratch/Paint Repairs Paintless dent repairs Alloy wheel repairs</text>
  </g>

  <!-- Back card -->
  <g class="card-back">
    <rect x="438" y="327" width="667" height="366" rx="40" fill="var(--card-edge)"/>
    <g clip-path="url(#back-clip)">
      <rect x="454" y="343" width="635" height="334" fill="url(#back-bg)"/>
      <path class="wave-top" d="M480 343 C620 370 760 390 900 420 C980 440 1040 460 1089 470 L1089 343 Z" fill="var(--wave-light)" opacity="0.9"/>
      <path class="wave-top-inner" d="M454 343 C600 400 760 420 880 450 C960 470 1030 485 1089 490 L1089 470 C1030 455 960 430 880 405 C760 375 620 355 520 343 Z" fill="var(--wave-mid)" opacity="0.6"/>
      <path class="wave-bottom" d="M454 482 C540 470 640 450 720 470 C820 500 860 560 950 560 C1010 560 1060 540 1089 525 L1089 630 C1060 650 1020 677 980 677 L454 677 Z" fill="var(--wave-light)"/>
      <path class="wave-shadow" d="M990 677 C1040 650 1070 620 1089 600 L1089 677 Z" fill="var(--plum-deep)"/>
    </g>

    <text class="title-text" x="782" y="415" font-size="46" text-anchor="middle"
          textLength="545" lengthAdjust="spacingAndGlyphs">Verdant QUICK Repairs Services</text>
    <text class="services-text" x="786" y="462" font-size="17" text-anchor="middle"
          textLength="491" lengthAdjust="spacingAndGlyphs">Bumper Repairs Scratch/Paint Repairs Paintless dent repairs Alloy wheel repairs</text>

    <g class="contact-name">
      <circle class="icon" cx="492" cy="515" r="7"/>
      <path class="icon" d="M480 531 C480 522 486 521 492 521 C498 521 504 522 504 531 Z"/>
      <text class="contact-text" x="526" y="531" font-size="25" textLength="160" lengthAdjust="spacingAndGlyphs">Martin K</text>
    </g>
    <g class="contact-phone">
      <rect x="484" y="557" width="16" height="28" rx="3" fill="none" stroke="var(--ink)" stroke-width="2.5"/>
      <circle class="icon" cx="492" cy="580" r="1.6"/>
      <text class="contact-text" x="526" y="583" font-size="25" textLength="214" lengthAdjust="spacingAndGlyphs">0427195063</text>
    </g>
    <g class="contact-email">
      <text class="contact-text" x="483" y="633" font-size="24">@</text>
      <text class="contact-text" x="518" y="633" font-size="24" textLength="545" lengthAdjust="spacingAndGlyphs">martin@harbisonmotors.com.au</text>
    </g>
  </g>
</svg>
</body>
</html>
```